Tandle Repair - Handyman and Home Repair Services

I need a business card/letterhead logo for my new handyman service in my local area. I'm happy for a logo design to be done prior to business card design so it can be incorporated on to the card, for which I'd be happy to pay more for. I'd like it to be modern and not using the typical pictures of tools and cartoon characters in dungarees! I like the idea of tools but in a more modern way i.e subtle background images in different shades to main colour. I do like the american retro designs and those that show age and patina for example, having an image half old, half new in its appearance to represent the repairing of things. Colours in mind are 1950's retro colours, ie using grey with pastel greens, red and cream. I'd like to break the mould and the stigma thats attached to these jobs and make it more cool and up to date. I hope this will attract interior designers and more modern businesses to use my services.

This is the logo design I like and would be happy for this idea and colours:

http://toast-a-roam.co.uk/wp-content/uploads/2011/01/t-r_logo600px.png

```html
<!DOCTYPE html>
<html lang="en">
<head>
<meta charset="utf-8">
<title>Tandle Repair – Business Card</title>
<link rel="stylesheet" href="https://fonts.googleapis.com/css2?family=Oswald:wght@500;600&display=swap">
<style>
  :root {
    --backdrop: #2e2a27;
    --card-grey: #58575a;
    --card-grey-light: #66656a;
    --card-grey-dark: #4a494c;
    --green: #8cc63f;
    --cream: #f3eec6;
    --white: #f4f4f2;
    --badge-dark: #2c2c2e;
  }
  * { box-sizing: border-box; margin: 0; padding: 0; }
  html, body {
    width: 1200px;
    height: 855px;
    overflow: hidden;
    background: var(--backdrop);
    font-family: "Oswald", "Arial Narrow", sans-serif;
  }
  .canvas {
    position: relative;
    width: 1200px;
    height: 855px;
  }

  /* ---------- shared card ---------- */
  .card {
    position: absolute;
    width: 500px;
    height: 290px;
    border-radius: 22px;
    background: linear-gradient(135deg, var(--card-grey-light), var(--card-grey) 45%, var(--card-grey-dark));
    overflow: hidden;
  }

  /* ---------- front card ---------- */
  .card--front { left: 70px; top: 110px; }

  .tool-backdrop {
    position: absolute;
    left: 60px;
    top: 40px;
    width: 300px;
    height: 210px;
    border-radius: 50%;
    background: radial-gradient(ellipse at center, rgba(60,60,62,0.55), rgba(88,87,90,0) 70%);
  }

  .brand-badge {
    position: absolute;
    left: 60px;
    top: 100px;
    width: 300px;
    height: 90px;
    display: flex;
    align-items: center;
    justify-content: center;
    gap: 12px;
  }
  .brand-badge__dot {
    width: 16px;
    height: 16px;
    border-radius: 50%;
    background: var(--green);
    flex: none;
  }
  .brand-badge__name {
    color: var(--green);
    font-weight: 600;
    font-size: 38px;
    letter-spacing: 1px;
    text-transform: uppercase;
    line-height: 1;
  }

  .edge-stripe {
    position: absolute;
    left: 432px;
    top: 0;
    width: 7px;
    height: 100%;
    background: var(--cream);
  }
  .web-address {
    position: absolute;
    left: 402px;
    top: 0;
    height: 100%;
    writing-mode: vertical-rl;
    transform: rotate(180deg);
    display: flex;
    align-items: center;
    justify-content: center;
    color: var(--green);
    font-weight: 600;
    font-size: 19px;
    letter-spacing: 1px;
  }

  /* ---------- back card ---------- */
  .card--back { left: 630px; top: 110px; }

  .card-logo {
    position: absolute;
    left: 26px;
    top: 112px;
    display: flex;
    align-items: center;
    gap: 7px;
  }
  .card-logo__dot {
    width: 9px;
    height: 9px;
    border-radius: 50%;
    background: var(--green);
  }
  .card-logo__name {
    color: var(--green);
    font-weight: 600;
    font-size: 17px;
    text-transform: uppercase;
    letter-spacing: 0.5px;
  }

  .divider {
    position: absolute;
    left: 190px;
    top: 30px;
    width: 1px;
    height: 230px;
    background: #6f8a4a;
  }

  .service-lines {
    position: absolute;
    left: 215px;
    top: 50px;
    text-transform: uppercase;
    font-weight: 600;
    line-height: 1.1;
  }
  .service-lines__title { color: var(--green); font-size: 27px; letter-spacing: 1px; }
  .service-lines__slogan { color: var(--white); font-size: 21px; letter-spacing: 0.5px; }

  .contact {
    position: absolute;
    left: 215px;
    top: 168px;
    text-transform: uppercase;
    font-weight: 600;
  }
  .contact__name { color: var(--green); font-size: 25px; letter-spacing: 1px; }
  .contact__phone {
    display: flex;
    align-items: center;
    gap: 8px;
    color: var(--white);
    font-size: 21px;
    font-weight: 500;
    letter-spacing: 1px;
  }
  .contact__phone svg { width: 18px; height: 18px; flex: none; }

  /* ---------- standalone logo lockup ---------- */
  .logo-lockup {
    position: absolute;
    left: 390px;
    top: 540px;
    width: 420px;
    height: 130px;
    display: flex;
    align-items: center;
    justify-content: center;
    gap: 16px;
  }
  .logo-lockup__dot {
    width: 20px;
    height: 20px;
    border-radius: 50%;
    background: var(--green);
  }
  .logo-lockup__name {
    color: var(--green);
    font-weight: 600;
    font-size: 44px;
    text-transform: uppercase;
    letter-spacing: 1.5px;
  }
</style>
</head>
<body>
<main class="canvas">

  <section class="card card--front" aria-label="Business card front">
    <div class="tool-backdrop" role="img" aria-label="Faint silhouettes of hand tools behind the brand name"></div>
    <div class="brand-badge">
      <span class="brand-badge__dot"></span>
      <span class="brand-badge__name">Tandle Repair</span>
    </div>
    <div class="web-address">www.tandlefix-homes.co.uk</div>
    <div class="edge-stripe"></div>
  </section>

  <section class="card card--back" aria-label="Business card back">
    <div class="card-logo">
      <span class="card-logo__dot"></span>
      <span class="card-logo__name">Tandle Repair</span>
    </div>
    <div class="divider"></div>
    <div class="service-lines">
      <p class="service-lines__title">Handyman Services</p>
      <p class="service-lines__slogan">From Repair to Install</p>
    </div>
    <div class="contact">
      <p class="contact__name">Owen Hartley</p>
      <p class="contact__phone">
        <svg viewBox="0 0 20 20" aria-hidden="true">
          <circle cx="10" cy="10" r="10" fill="#8cc63f"/>
          <rect x="6.5" y="4" width="7" height="12" rx="1.5" fill="#58575a"/>
          <rect x="7.8" y="5.6" width="4.4" height="7" fill="#8cc63f"/>
        </svg>
        07700 900418
      </p>
    </div>
  </section>

  <section class="logo-lockup" aria-label="Tandle Repair logo">
    <span class="logo-lockup__dot"></span>
    <span class="logo-lockup__name">Tandle Repair</span>
  </section>

</main>
</body>
</html>
```